Web Design Project

Need a start website for a new company called StoneRiver.

We help large data center customers optimize and transform their data centers.

We have't gotten a logo yet but are in the process of running a separate contest to do that here on ArtHive.

Will post the logo shortly. Our logo is blue and orange predominantly. Haven't gotten a full color scheme together just yet.

Ultimately we are to be a reseller partner of QMB http://www.qmb-example.com and would like the website to somewhat look-and-feel like theirs. At least enough that a person could easily go from one to the other.
Updates

Reason: Again not sure why this is coming up as a deadline of tomorrow. Extended the deadline out as far as ArtHive will allow. Mark

Just posted the logos to the page as well as committed the project payout as well. Thank you!

Was asked how much coding outside of a basic website required. At this time, the most complex thing might be a CSS style sheet so we can change / tweak colors or fonts. Beyond that it should be fairly simply and straight-forward with the most complex thing being links to "mailto:info" and stuff like that. Mark

Top level choices for 2nd level pages should be as follows: Products Solutions Services Partners About (or About Us) Not sure of the final order of these but that'll be all of them There should also be an area on the main page for partner logos which will link directly to their website. This could be at the bottom of the page or else where. It should be below the main heading part. We do not anticipate having more than 5 or 6 key / strategic partners that will provide logo approval.

Target Market(s)

Our target customers of our business are organizations with large data centers looking at optimizing their current data centers, relocating or consolidating their data centers into new data centers.

Typically our buyer will be the CIO, CTO or CFO of the organization.

Industry/Entity Type

It Company

Font styles to use
Sans Serif

Requirements
Should not have
• No flash or anything difficult to maintain at least initially.

```html
<!DOCTYPE html>
<html lang="en">
<head>
<meta charset="utf-8">
<title>StoneRiver – Data Center Solutions</title>
<link href="https://fonts.googleapis.com/css2?family=Lato:ital,wght@0,300;0,400;0,700;1,400&family=Roboto:wght@400&display=swap" rel="stylesheet">
<style>
:root{
  --blue:#1f7fc2;
  --orange:#f07f22;
  --ink:#222;
  --text:#444;
  --band:#f1f1f1;
  --line:#dcdcdc;
  --partner:#d4d8dd;
  --footer:#333335;
  --footer-bar:#232325;
}
*{box-sizing:border-box;margin:0;padding:0}
html,body{width:797px;height:1200px;overflow:hidden;background:#fff}
body{font-family:'Lato',sans-serif;color:var(--text);position:relative}
a{color:inherit;text-decoration:none}
.abs{position:absolute}

/* header */
.site-header{position:absolute;left:0;top:0;width:797px;height:50px;background:linear-gradient(#fff,#f0f0f0);border-top:2px solid var(--blue)}
.brand{position:absolute;left:92px;top:12px;display:flex;align-items:center;gap:7px}
.brand-dot{width:28px;height:28px;border-radius:50%;background:var(--orange)}
.brand-name{font-size:24px;font-weight:700;color:var(--blue);letter-spacing:-.3px}
.phone{position:absolute;right:91px;top:4px;display:flex;align-items:center;gap:6px;font-size:15px;color:var(--ink)}
.main-nav{position:absolute;right:89px;top:31px;display:flex;gap:9px;font-size:10.5px;color:var(--ink);white-space:nowrap}
.main-nav a.active{color:var(--blue)}

/* hero */
.hero{position:absolute;left:0;top:50px;width:797px;height:298px;background:linear-gradient(90deg,#f4f4f4 0%,#cfcfcf 18%,#4a4a4a 40%,#1f1f1f 70%,#111 100%)}
.hero-caption{position:absolute;left:88px;top:263px;width:622px;height:35px;background:rgba(60,60,60,.75);color:#fff;font-family:'Roboto',sans-serif;font-size:15.5px;line-height:35px;padding-left:6px;letter-spacing:.2px}
.hero-dots{position:absolute;left:648px;top:276px;display:flex;gap:6px}
.hero-dots span{width:10px;height:10px;background:#fff}
.hero-dots span.on{background:var(--orange)}

/* welcome */
.welcome{position:absolute;left:0;top:348px;width:797px;text-align:center}
.welcome h1{margin-top:21px;font-weight:300;font-size:20px;color:var(--ink);display:flex;justify-content:center;align-items:center;gap:8px}
.welcome h1 b{font-weight:700;color:var(--blue)}
.welcome h1 i{display:inline-block;width:28px;height:28px;border-radius:50%;background:var(--orange)}
.welcome .lead{margin-top:12px;font-style:italic;font-size:9.5px;color:var(--blue)}
.welcome p.body{width:636px;margin:3px auto 0;font-size:9px;line-height:14.5px;color:#333}
.btn{display:inline-block;background:var(--blue);color:#fff;font-weight:700;font-size:8.5px;border-radius:3px;box-shadow:0 3px 3px rgba(0,0,0,.2);white-space:nowrap}
.welcome .btn{margin-top:12px;padding:0 6px;height:24px;line-height:24px;width:63px}

/* services */
.services{position:absolute;left:0;top:512px;width:797px;height:230px;background:var(--band)}
.service{position:absolute;top:36px;width:143px;height:175px;background:#fff;border:1px solid var(--line)}
.service .badge{position:absolute;left:53px;top:-20px;width:36px;height:36px;border-radius:50%;background:var(--orange);border:3px solid #d5d5d5}
.service .thumb{position:absolute;left:10px;top:7px;width:121px;height:81px}
.service h3{position:absolute;left:10px;top:98px;font-size:11.5px;font-weight:400;color:var(--ink)}
.service p{position:absolute;left:10px;top:116px;width:125px;font-size:8.5px;line-height:12px;color:#444}
.service .btn{position:absolute;left:10px;top:148px;width:44px;height:16px;line-height:16px;text-align:center;font-weight:400;border-radius:0}

/* feeds */
.col-title{position:absolute;top:762px;font-size:14px;font-weight:400;color:var(--ink)}
.col-rule{position:absolute;top:782px;height:1px;background:var(--line)}
.col-rule::before{content:"";position:absolute;left:0;top:0;width:40px;height:1px;background:var(--orange)}
.arrows{position:absolute;top:765px;font-size:11px;color:#999;letter-spacing:2px}
.news-item{position:absolute;left:88px;width:190px}
.date{position:absolute;left:0;top:0;width:27px;text-align:center}
.date .m{background:var(--orange);color:#fff;font-size:7px;height:10px;line-height:10px}
.date .d{background:#333;color:#fff;font-size:13px;font-weight:700;height:18px;line-height:18px}
.news-item h4{position:absolute;left:37px;top:0;font-size:8.5px;font-weight:700;color:var(--ink);white-space:nowrap}
.news-item p{position:absolute;left:37px;top:11px;width:150px;font-size:8px;line-height:11.5px}
.col-divider{position:absolute;top:790px;width:1px;height:100px;background:var(--line)}
.tweet{position:absolute;left:294px;width:215px;font-size:7.8px;line-height:10.5px;color:#333}
.tweet .hl{color:var(--blue)}
.tweet .url{color:var(--orange)}
.event{position:absolute;left:535px;width:175px}
.event .tag{position:absolute;left:0;top:0;width:44px;height:24px;background:#1d4e8c}
.event h4{position:absolute;left:50px;top:0;font-size:8.5px;font-weight:700;color:var(--ink);white-space:nowrap}
.event p{position:absolute;left:50px;top:11px;font-size:8px;line-height:9.5px;white-space:nowrap}
.event a{position:absolute;left:50px;top:29px;font-size:8px;font-weight:700;color:var(--orange)}

/* partners */
.partners{position:absolute;left:0;top:898px;width:797px;height:40px;background:#fff;border-top:1px solid var(--line)}
.partners h2{position:absolute;left:88px;top:13px;font-size:11px;font-weight:400;color:var(--ink)}
.partner-list{position:absolute;left:190px;top:9px;display:flex;gap:14px}
.partner-list a{width:74px;height:22px;background:var(--partner);border-radius:2px}

/* testimonials */
.testimonials{position:absolute;left:0;top:938px;width:797px;height:105px;background:#f6f6f6}
.testimonials h2{position:absolute;left:0;width:797px;top:6px;text-align:center;font-weight:400;font-size:15px;color:var(--ink)}
.testimonials h2::before,.testimonials h2::after{content:"";position:absolute;top:10px;width:160px;height:1px;background:#d0d0d0}
.testimonials h2::before{left:160px}.testimonials h2::after{right:170px}
.avatar{position:absolute;left:93px;top:32px;width:57px;height:57px;border-radius:50%;border:2px solid var(--blue);background:radial-gradient(circle at 50% 40%,#f3d9b8,#d9b37b 60%,#c9d8e6 100%)}
.quote{position:absolute;left:167px;top:32px;width:535px;font-style:italic;font-size:8.4px;line-height:13px;color:#333}
.quote .mark{color:#e8a56a;font-size:15px;line-height:0;font-style:normal;font-weight:700}
.author{position:absolute;left:167px;top:89px;font-size:8.5px;font-weight:700;color:var(--blue)}
.t-dots{position:absolute;left:673px;top:92px;display:flex;gap:2px}
.t-dots span{width:5px;height:5px;border-radius:50%;background:var(--blue)}
.t-dots span.on{background:var(--orange)}

/* footer */
.site-footer{position:absolute;left:0;top:1043px;width:797px;height:132px;background:var(--footer);border-top:2px solid var(--blue);color:#ddd}
.site-footer h5{position:absolute;top:12px;font-size:11.5px;font-weight:400;color:#fff}
.f-rule{position:absolute;top:31px;height:1px;background:#4a4a4c}
.f-sep{position:absolute;top:15px;width:1px;height:100px;background:#444}
.quick-links{position:absolute;left:88px;top:36px;list-style:none;font-size:8.5px;line-height:12.3px;color:#fff}
.quick-links li::before{content:"›";color:#aaa;margin-right:6px}
.contact-row{position:absolute;left:205px;display:flex;gap:9px;font-size:8.5px;line-height:10px;color:#fff}
.contact-row svg{flex:none;margin-top:1px}
.newsletter p{position:absolute;left:413px;top:40px;width:150px;font-size:8px;line-height:12px;color:#fff}
.email-field{position:absolute;left:413px;top:68px;width:139px;height:18px;background:#fff;font-size:7px;color:#888;line-height:18px;padding-left:4px}
.subscribe{position:absolute;left:413px;top:94px;width:69px;height:19px;background:var(--orange);color:#fff;font-size:9px;font-weight:700;text-align:center;line-height:19px}
.social{position:absolute;left:607px;top:43px;display:flex;gap:8px}
.social span{width:19px;height:19px;border-radius:50%;background:#555}
.social span.on{background:var(--blue)}
.foot-brand{position:absolute;left:607px;top:84px;display:flex;align-items:center;gap:5px;font-size:15px;font-weight:700;color:#666}
.foot-brand i{width:20px;height:20px;border-radius:50%;background:#555}
.copyright{position:absolute;left:0;top:1175px;width:797px;height:25px;background:var(--footer-bar);color:#ccc;font-size:8px;text-align:center;line-height:25px}
</style>
</head>
<body>

<header class="site-header">
  <div class="brand"><span class="brand-dot"></span><span class="brand-name">StoneRiver</span></div>
  <div class="phone">
    <svg width="14" height="14" viewBox="0 0 14 14"><circle cx="7" cy="7" r="6.2" fill="none" stroke="#1f7fc2" stroke-width="1.3"/><path d="M4.6 3.8l1.3-.2.7 1.7-.9.7a5 5 0 0 0 2.3 2.3l.7-.9 1.7.7-.2 1.3c-3.3.3-5.9-2.3-5.6-5.6z" fill="#1f7fc2"/></svg>
    555-204-7731
  </div>
  <nav class="main-nav">
    <a class="active" href="#">HOME</a><a href="#">PRODUCTS</a><a href="#">SOLUTIONS</a><a href="#">SERVICES</a><a href="#">PARTNERS</a><a href="#">ABOUT US</a><a href="#">CONTACT US</a>
  </nav>
</header>

<section class="hero" role="img" aria-label="Photograph of a long corridor of server racks in a data center">
  <div class="hero-caption">WE BUILD DATA CENTERS IN WHICH YOU CAN BUILD YOUR BUSINESS</div>
  <div class="hero-dots"><span></span><span class="on"></span><span></span><span></span></div>
</section>

<section class="welcome">
  <h1><i></i>WELCOME TO <b>StoneRiver</b></h1>
  <p class="lead">Lorem ipsum dolor sit amet, consectetur adipiscing eli Vestibulum efficitur pellentesque mi, ut vestibulum mauris sagittis at.</p>
  <p class="body">Aliquam vitae magna aliquet, molestie est eget, ultricies arcu. Nunc non luctus turpis, et sollicitudin sem. In at vehicula tellus. Nulla vel eleifend nulla, quis ultrices metus. Nunc finibus nisi ac congue tempor. Nulla elementum, leo non vehicula lacinia, velit libero hendrerit purus, sed feugiat felis orci id erat. Cras ultrices vehicula lectus a porttitor. Nunc eu enim at sem varius aliquet Vestibulum eu dolor erat. Aenean luctus venenatis</p>
  <a class="btn" href="#">READ MORE</a>
</section>

<section class="services">
  <article class="service" style="left:87px">
    <span class="badge"></span>
    <div class="thumb" role="img" aria-label="Photograph of a blue-lit server aisle" style="background:linear-gradient(#0a1440,#2a4fd0 50%,#0a1440)"></div>
    <h3>DEDICATED SERVER</h3>
    <p>Lorem ipsum dolor consectetur adipiscing elit estibueff</p>
    <a class="btn" href="#">MORE</a>
  </article>
  <article class="service" style="left:247px">
    <span class="badge"></span>
    <div class="thumb" role="img" aria-label="Photograph of rack-mounted VPS servers" style="background:linear-gradient(#f4f4f4,#5a5a5a 55%,#cfcfcf)"></div>
    <h3>VPS HOSTING</h3>
    <p>Lorem ipsum dolor consectetur adipiscing elit estibueff</p>
    <a class="btn" href="#">MORE</a>
  </article>
  <article class="service" style="left:407px">
    <span class="badge"></span>
    <div class="thumb" role="img" aria-label="Photograph of dark cloud server cabinets" style="background:linear-gradient(90deg,#1a1a1a,#3a3a3a,#0f0f0f)"></div>
    <h3>CLOUD SERVERS</h3>
    <p>Lorem ipsum dolor consectetur adipiscing elit estibueff</p>
    <a class="btn" href="#">MORE</a>
  </article>
  <article class="service" style="left:567px">
    <span class="badge"></span>
    <div class="thumb" role="img" aria-label="Illustration of a digital interface for managed services" style="background:linear-gradient(135deg,#1b2f55,#4f7fae 60%,#22385f)"></div>
    <h3>MANAGED SERVICES</h3>
    <p>Lorem ipsum dolor consectetur adipiscing elit estibueff</p>
    <a class="btn" href="#">MORE</a>
  </article>
</section>

<!-- news -->
<h2 class="col-title" style="left:88px">NEWS</h2>
<span class="arrows" style="left:258px">‹ ›</span>
<div class="col-rule" style="left:88px;width:190px"></div>
<div class="news-item" style="top:800px">
  <div class="date"><div class="m">NOV</div><div class="d">04</div></div>
  <h4>Lorem ipsum dolor sit amet .</h4>
  <p>Lorem ipsum dol adipiscing elit, seder or sit amet, consectetuer adipiscing elit.</p>
</div>
<div class="news-item" style="top:857px">
  <div class="date"><div class="m">NOV</div><div class="d">04</div></div>
  <h4>Lorem ipsum dolor sit amet .</h4>
  <p>Lorem ipsum dol adipiscing elit, seder or sit amet, consectetuer adipiscing elit.</p>
</div>
<div class="col-divider" style="left:283px"></div>

<!-- social feed -->
<h2 class="col-title" style="left:294px;font-size:13px;top:764px">
  <span style="display:inline-block;width:9px;height:9px;border-radius:50%;background:var(--blue);margin-right:4px"></span>Follow Us On CHIRPLINE
</h2>
<span class="arrows" style="left:500px">‹ ›</span>
<div class="col-rule" style="left:294px;width:220px"></div>
<p class="tweet" style="top:799px"><span class="hl">StoneRiver</span> ON CHIRPLINE Follow us on CHIRPLINE<br>Find out why testing and validation is the secret sauce of true convergence in @mreyes's #StoneRiver blog<br><span class="url">http://lnk.example/q7Rm2Kx</span></p>
<div class="abs" style="left:294px;top:848px;width:215px;height:1px;background:var(--line)"></div>
<p class="tweet" style="top:857px">K7 Application Delivery Controllers Certified as <span class="hl">#StoneRiver</span><br>#Gblock Ready<br><span class="url">http://lnk.example/w3Tp9Zd @k7systems</span></p>
<div class="col-divider" style="left:520px"></div>

<!-- events -->
<h2 class="col-title" style="left:535px">EVENTS</h2>
<span class="arrows" style="left:697px">‹ ›</span>
<div class="col-rule" style="left:535px;width:175px"></div>
<div class="event" style="top:798px">
  <span class="tag"></span>
  <h4>Vantage Summit</h4>
  <p>TechForum 2014 Nov 09, 2014<br>Nov 13, 2014, Barcelona, Spain</p>
  <a href="#">LEARN MORE</a>
</div>
<div class="event" style="top:852px">
  <span class="tag"></span>
  <h4>Vantage Summit</h4>
  <p>TechForum 2014 Nov 09, 2014<br>Nov 13, 2014, Barcelona, Spain</p>
  <a href="#">LEARN MORE</a>
</div>

<section class="partners">
  <h2>Our Partners</h2>
  <div class="partner-list">
    <a href="#" aria-label="Partner 1"></a><a href="#" aria-label="Partner 2"></a><a href="#" aria-label="Partner 3"></a><a href="#" aria-label="Partner 4"></a><a href="#" aria-label="Partner 5"></a><a href="#" aria-label="Partner 6"></a>
  </div>
</section>

<section class="testimonials">
  <h2>Client Testimonials</h2>
  <div class="avatar" role="img" aria-label="Portrait photograph of the client"></div>
  <p class="quote"><span class="mark">“</span> Lorem ipsdolor sit amet, consectetur adipiscing elit. Donec sit amet nulla vitae tortor iaculis commodo. Nulla interdum dui vitae lectus malesuada ac dignissim mi vehicula. Nullam ornare vulputate sem vitae convallis. Proin et faucibus eros. Nam id rutrum risus, quis eleifend tortor. Nulla scelerisque vitae ante vitae, rhoncus pellentesque turpis. Donec feugiat malesuada justo, quis porta urna egestas nec. Duis nec lobortis justo, ac varius ante. <span class="mark">”</span></p>
  <div class="abs" style="left:167px;top:84px;width:535px;height:1px;background:#e2e2e2"></div>
  <div class="author">Miss. Clara Bennett</div>
  <div class="t-dots"><span></span><span class="on"></span><span></span><span></span></div>
</section>

<footer class="site-footer">
  <h5 style="left:88px">Quick Links</h5>
  <div class="f-rule" style="left:88px;width:80px"></div>
  <ul class="quick-links">
    <li>Home</li><li>Products</li><li>Solutions</li><li>Services</li><li>Partners</li><li>About Us</li><li>Contact Us</li>
  </ul>
  <div class="f-sep" style="left:178px"></div>

  <h5 style="left:205px">Contact Information</h5>
  <div class="f-rule" style="left:205px;width:165px"></div>
  <div class="contact-row" style="top:47px">
    <svg width="8" height="11" viewBox="0 0 8 11"><path d="M4 0a4 4 0 0 1 4 4c0 3-4 7-4 7S0 7 0 4a4 4 0 0 1 4-4z" fill="#fff"/><circle cx="4" cy="4" r="1.5" fill="#333"/></svg>
    <span>Lorem ipsum dolor consectetuer<br>adipiscing elit, sed diam nonummy<br>bitasa street:395001</span>
  </div>
  <div class="contact-row" style="top:84px">
    <svg width="10" height="10" viewBox="0 0 10 10"><path d="M1.5 1l2-.5 1 2.3-1.2.9a5 5 0 0 0 2.8 2.8l.9-1.2 2.3 1-.5 2C4.5 8.6 1.4 5.5 1.5 1z" fill="#fff"/></svg>
    <span>555-204-7731</span>
  </div>
  <div class="contact-row" style="top:106px">
    <svg width="10" height="8" viewBox="0 0 10 8"><rect width="10" height="8" fill="#fff"/><path d="M0 0l5 4 5-4" fill="none" stroke="#333" stroke-width="1"/></svg>
    <span>info@stoneriver.com</span>
  </div>
  <div class="f-sep" style="left:385px"></div>

  <div class="newsletter">
    <h5 style="left:413px">Newsletter Sign Up</h5>
    <div class="f-rule" style="left:413px;width:150px"></div>
    <p>Lorem ipsudolor sit coec adipisdfghscing elitsite amet</p>
    <div class="email-field">Email Address</div>
    <div class="subscribe">SUBSCRIBE</div>
  </div>
  <div class="f-sep" style="left:583px"></div>

  <h5 style="left:607px">Follow Us</h5>
  <div class="f-rule" style="left:607px;width:104px"></div>
  <div class="social"><span></span><span class="on"></span><span></span><span></span></div>
  <div class="foot-brand"><i></i>StoneRiver</div>
</footer>
<div class="copyright">© 2014. StoneRiver. All Rights Reserved.</div>

</body>
</html>
```